Company Business Card, for Harborveldt.com Floating homes and Marinas

To design a new great looking business card that follows some how the theme of our business and website. Harborveldt.com

I have attached our logo and a copy of our existing card (boring)

   We appreciate everyones efforts so far there are some very interesting designs. We are thinking that our company is more than just a Marina manufacturer, we build many different floating products and we would like our card to show case those products. There has been one card that has done this, and we are leaning towards that design. We prefer that our logo and company name are proportional on the card, and our mission statement be also shown. Thank you                                

                                   

 We do like your designs, on the back of the card  we want to show all 6 different product types as shown on the front of our website.

                                   

Sorry some designers have the images on the front, and that is okay as well. We just want on the card all 6 areas that we manufacture.

• Must have a new look, maybe nautical, following the theme of what our company manufactures.

Logo
Company name: Consolidated Pontoon Dockworks Group, Inc.

Website: www.HarborVeldt.com

Employee name & title

Mission statement: "Craftsmanship is the keel that carries every voyage"

Our Address: 4718 Quillan Avenue, Delta, B.C. Canada, V3K 2R7

• Colour and unique presentation,

```html
<!DOCTYPE html>
<html lang="en">
<head>
<meta charset="utf-8">
<title>HarborVeldt Business Card</title>
<link rel="stylesheet" href="https://fonts.googleapis.com/css2?family=Jost:ital,wght@0,300;0,400;0,600;1,400&display=swap">
<style>
  :root {
    --stage: #2b2b2d;
    --paper: #f1f0ee;
    --charcoal: #2a2c31;
    --ink: #232323;
    --grey-text: #555555;
    --red: #d4202a;
    --light: #e9e9e9;
    --sea-deep: #2f4a5e;
    --sea-light: #6f8fa6;
  }
  * { box-sizing: border-box; margin: 0; padding: 0; }
  html, body {
    width: 1200px; height: 900px; overflow: hidden;
    background: var(--stage);
    font-family: "Jost", "Futura", sans-serif;
  }
  .stage {
    width: 1200px; height: 900px;
    display: flex; flex-direction: column;
    align-items: center; justify-content: center; gap: 48px;
  }
  .card {
    position: relative;
    width: 640px; height: 366px;
    overflow: hidden;
  }

  /* Front */
  .card-front { background: var(--paper); color: var(--ink); }
  .brand-box {
    position: absolute; left: 44px; top: 44px;
    width: 236px; height: 98px;
    border: 3px solid var(--red);
    display: flex; align-items: center; justify-content: center; gap: 10px;
  }
  .brand-mark { width: 14px; height: 14px; background: var(--red); }
  .brand-name {
    font-weight: 600; font-size: 30px; letter-spacing: 1px; color: var(--ink);
  }
  .company-name {
    position: absolute; left: 330px; top: 42px; width: 230px;
    font-weight: 300; font-size: 19px; line-height: 1.08;
    letter-spacing: 1.5px; text-transform: uppercase; color: var(--grey-text);
  }
  .person {
    position: absolute; left: 44px; top: 222px; width: 236px; text-align: center;
  }
  .person-name {
    font-weight: 600; font-size: 17px; letter-spacing: 1.5px; text-transform: uppercase;
  }
  .person-title {
    font-style: italic; font-size: 14px; color: var(--red); margin-top: 2px;
  }
  .contact {
    position: absolute; left: 330px; top: 226px;
    font-size: 13px; line-height: 1.4; color: var(--grey-text); font-style: normal;
  }
  .contact-label { color: var(--red); font-weight: 600; }
  .front-band {
    position: absolute; left: 0; right: 0; bottom: 0; height: 20px; display: flex;
  }
  .front-band .band-dark { width: 50%; background: var(--ink); }
  .front-band .band-red { flex: 1; background: var(--red); }

  /* Back */
  .card-back {
    background: var(--charcoal);
    display: flex; flex-direction: column; align-items: center;
  }
  .card-back .brand-box {
    position: static; margin-top: 34px;
    width: 220px; height: 100px;
    background: var(--light); border: 4px solid var(--red);
  }
  .mission {
    margin-top: 26px;
    font-weight: 400; font-size: 22px; line-height: 1.2;
    letter-spacing: 1px; text-transform: uppercase;
    color: var(--red); text-align: center;
  }
  .website {
    margin-top: 16px; font-size: 16px; letter-spacing: 0.5px; color: var(--light);
  }
  .website-domain { color: var(--red); }
  .product-row {
    margin-top: 22px; display: flex; gap: 8px;
  }
  .product-tile {
    width: 84px; height: 46px;
    background: linear-gradient(180deg, var(--sea-light), var(--sea-deep));
    border-top: 2px solid var(--red);
  }
</style>
</head>
<body>
<main class="stage">
  <section class="card card-front" aria-label="Business card front">
    <div class="brand-box">
      <span class="brand-mark"></span>
      <span class="brand-name">HarborVeldt</span>
    </div>
    <h1 class="company-name">Consolidated Pontoon Dockworks Group, Inc.</h1>
    <div class="person">
      <p class="person-name">Lucan Verhoeven</p>
      <p class="person-title">Senior Project Manager</p>
    </div>
    <address class="contact">
      4718 Quillan Avenue, Delta<br>
      B.C. Canada, V3K 2R7<br>
      <span class="contact-label">T:</span> 604.555.0182<br>
      <span class="contact-label">E:</span> lucan@HarborVeldt.com
    </address>
    <div class="front-band"><span class="band-dark"></span><span class="band-red"></span></div>
  </section>

  <section class="card card-back" aria-label="Business card back">
    <div class="brand-box">
      <span class="brand-mark"></span>
      <span class="brand-name">HarborVeldt</span>
    </div>
    <p class="mission">Craftsmanship is the keel<br>that carries every voyage</p>
    <p class="website">www.<span class="website-domain">HarborVeldt</span>.com</p>
    <div class="product-row">
      <div class="product-tile" role="img" aria-label="Photo of a floating home"></div>
      <div class="product-tile" role="img" aria-label="Photo of a marina"></div>
      <div class="product-tile" role="img" aria-label="Photo of a floating dock"></div>
      <div class="product-tile" role="img" aria-label="Photo of a breakwater"></div>
      <div class="product-tile" role="img" aria-label="Photo of a boathouse"></div>
      <div class="product-tile" role="img" aria-label="Photo of a floating walkway"></div>
    </div>
  </section>
</main>
</body>
</html>
```